Powerpoint Template for a cool IT Recruiting and Consulting Company

We need to have a PowerPoint template designed for our company. We are a Technology Consulting and Recruiting company in Canada.

I'm not looking for an explosion of colours, stay elegant and sharp.

The message that it needs to portray a cool tech company utilizing the blue in our logo but also professionalism and an excitement feel about it that makes clients want to do business with us.

I have attached 2 screenshots of the logo options and also the PDF of them.

Looking forward to seeing the results.

Target Market(s)

We sell our services to Banks, Government and other Tech Companies

Industry/Entity Type

It Service

Font styles to use
Sans Serif

Colors
0592cd

Requirements
Must have
• Logo
Nice to have
Should not have
• Lots of colours

```html
<!DOCTYPE html>
<html lang="en">
<head>
<meta charset="utf-8">
<title>Corvant Presentation Template</title>
<link href="https://fonts.googleapis.com/css2?family=Raleway:wght@300;400;500;600;700&display=swap" rel="stylesheet">
<style>
:root{
  --blue:#4a7aab;
  --blue-dark:#3c6892;
  --ink:#2e2e2e;
  --black:#111;
  --grey:#7b7b7b;
  --grey-light:#bdbdbd;
  --text:#9a9a9a;
  --rule:#e3e3e3;
  --page:#ffffff;
}
*{box-sizing:border-box;margin:0;padding:0}
html,body{width:695px;height:1200px;overflow:hidden;background:var(--page)}
body{font-family:"Raleway",Arial,sans-serif;position:relative}
.slide{position:absolute;width:229px;height:131px;background:#fff;overflow:hidden;box-shadow:0 0 0 .6px #dcdcdc}
.c1{left:1px}.c2{left:233px}.c3{left:465px}
.r1{top:1px}.r2{top:134px}.r3{top:267px}.r4{top:400px}.r5{top:533px}.r6{top:666px}.r7{top:799px}.r8{top:932px}.r9{top:1065px}
.abs{position:absolute}
.heading{position:absolute;left:11px;top:9px;font-size:7px;font-weight:600;color:var(--ink)}
.txt{font-size:3px;line-height:1.5;color:var(--text)}
.txt-w{font-size:3px;line-height:1.5;color:#fff}
.lead{font-size:4.6px;line-height:1.35;color:var(--blue)}
.label{font-size:3.6px;color:var(--blue);font-weight:500}
.footer{position:absolute;left:0;right:0;bottom:0;height:13px}
.brand{position:absolute;left:11px;bottom:3px;display:flex;align-items:center;gap:2px;font-size:6.4px;font-weight:700;color:var(--blue)}
.brand .dot{width:5px;height:5px;border-radius:50%;background:var(--blue)}
.copy{position:absolute;left:0;right:0;bottom:5px;text-align:center;font-size:2.6px;color:var(--text)}
.pager{position:absolute;right:9px;bottom:4px;width:6px;height:6px;border:.6px solid var(--blue);border-radius:50%}
.photo{position:absolute}
.ph-office{background:linear-gradient(135deg,#c9d3dc,#7f8d99 55%,#4f5d69)}
.ph-person{background:radial-gradient(circle at 50% 40%,#d7c2b0,#8d8a86 70%,#5b5f63)}
.ph-desk{background:linear-gradient(160deg,#e7ecf0,#aab6c0 60%,#6d7a86)}
.ph-blue{background:linear-gradient(135deg,#5f8cb8,#3e6a96)}
.round{border-radius:50%}
.blue-band{position:absolute;background:var(--blue)}
.icon-ring{position:absolute;width:13px;height:13px;border-radius:50%;border:.7px solid #fff}
.bullet-icon{position:absolute;width:7px;height:7px;border-radius:50%}
.price-card{position:absolute;background:#fff;box-shadow:0 0 2px rgba(0,0,0,.2)}
.price-head{height:16px;color:#fff;font-size:7px;text-align:center;padding-top:2px;line-height:1}
.price-head small{display:block;font-size:2.4px;margin-top:1px}
.price-line{font-size:2.6px;color:var(--text);text-align:center;padding:2px 0;border-bottom:.3px solid var(--rule);margin:0 5px}
table.data{border-collapse:collapse;font-size:2.6px;color:#777;width:100%}
table.data th{background:var(--blue);color:#fff;font-weight:500;padding:1.2px 3px;text-align:left}
table.data td{padding:1.2px 3px;border-bottom:.3px solid #e8e8e8}
table.data tr:nth-child(even) td{background:#eef2f6}
.member-name{font-size:3.8px;color:var(--ink)}
.member-role{font-size:2.6px;color:var(--blue)}
.white-title{color:#fff;font-weight:500}
.tl-line{position:absolute;left:114px;width:.6px;background:#c9d6e3}
.tl-node{position:absolute;width:8px;height:8px;border-radius:50%;border:.8px solid var(--blue);background:#fff}
.big-num{font-size:7px;font-weight:600;color:var(--ink)}
</style>
</head>
<body>

<!-- Row 1 -->
<section class="slide c1 r1">
  <h2 class="heading">Three Column Description</h2>
  <p class="abs lead" style="left:12px;top:32px;width:170px">This is place for your header text. Insert your text here, just replace this text with your own text</p>
  <p class="abs txt" style="left:12px;top:48px;width:62px">Place a short summary of your service here. Describe what sets the team apart and why clients choose you for their next project.<br><br>Keep each column brief and focused.</p>
  <p class="abs txt" style="left:86px;top:48px;width:62px">Place a short summary of your service here. Describe what sets the team apart and why clients choose you for their next project.<br><br>Keep each column brief and focused.</p>
  <p class="abs txt" style="left:160px;top:48px;width:62px">Place a short summary of your service here. Describe what sets the team apart and why clients choose you for their next project.<br><br>Keep each column brief and focused.</p>
  <div class="footer"><div class="brand"><span class="dot"></span>Corvant</div><div class="copy">© Copyright 2024 Corvant. All rights reserved</div><div class="pager"></div></div>
</section>

<section class="slide c2 r1">
  <h2 class="heading">Our Team</h2>
  <div class="photo ph-person round" role="img" aria-label="Portrait of team leader" style="left:97px;top:22px;width:35px;height:35px"></div>
  <p class="abs member-name" style="left:0;right:0;top:62px;text-align:center">Mr. Evan Hale</p>
  <p class="abs member-role" style="left:0;right:0;top:67px;text-align:center">CEO</p>
  <p class="abs txt" style="left:75px;width:80px;top:72px;text-align:center">Short biography of the team leader goes here, with focus and key strengths.</p>
  <div class="abs" style="left:101px;top:88px;display:flex;gap:2px">
    <span class="bullet-icon" style="position:static;width:4px;height:4px;background:var(--blue)"></span>
    <span class="bullet-icon" style="position:static;width:4px;height:4px;background:var(--blue)"></span>
    <span class="bullet-icon" style="position:static;width:4px;height:4px;background:var(--blue)"></span>
    <span class="bullet-icon" style="position:static;width:4px;height:4px;background:var(--blue)"></span>
  </div>
  <div class="footer"><div class="brand"><span class="dot"></span>Corvant</div><div class="copy">© Copyright 2024 Corvant. All rights reserved</div><div class="pager"></div></div>
</section>

<section class="slide c3 r1" style="background:var(--blue)">
  <div class="photo" role="img" aria-label="Faded office workspace background" style="inset:0;background:linear-gradient(120deg,rgba(255,255,255,.08),rgba(255,255,255,0) 60%)"></div>
  <div class="abs round" style="left:96px;top:-18px;width:38px;height:38px;background:#fff;display:flex;align-items:flex-end;justify-content:center;padding-bottom:7px">
    <span style="font-size:4px;font-weight:700;color:var(--blue)">Corvant</span>
  </div>
  <p class="abs white-title" style="left:0;right:0;top:72px;text-align:center;font-size:10px;font-weight:600">THIS IS YOUR DIVIDER PAGE</p>
  <p class="abs txt-w" style="left:0;right:0;top:87px;text-align:center">Your Subtitle Goes Here</p>
</section>

<!-- Row 2 -->
<section class="slide c1 r2">
  <h2 class="heading">Monthly Subscription</h2>
  <div class="abs" style="right:10px;top:7px;display:flex;flex-direction:column;align-items:center;gap:1px">
    <span class="round" style="width:6px;height:6px;border:.7px solid var(--blue)"></span>
    <span style="font-size:4px;font-weight:700;color:var(--blue)">Corvant</span>
  </div>
  <div class="blue-band" style="left:0;right:0;top:56px;bottom:0"></div>
  <div class="price-card" style="left:37px;top:36px;width:44px;height:60px">
    <div class="price-head" style="background:var(--grey)">$300<small>per month</small></div>
    <div class="price-line">Registration</div><div class="price-line">Page Development</div><div class="price-line">1 User</div><div class="price-line">Free Update</div>
  </div>
  <div class="price-card" style="left:87px;top:33px;width:58px;height:66px">
    <div class="price-head" style="background:var(--blue);height:19px;padding-top:3px">$900<small>per month</small></div>
    <div class="price-line">Business Edition</div><div class="price-line">Page Development</div><div class="price-line">6 User</div><div class="price-line">Free Update</div>
  </div>
  <div class="price-card" style="left:151px;top:36px;width:44px;height:60px">
    <div class="price-head" style="background:var(--black)">$400<small>per month</small></div>
    <div class="price-line">Registration</div><div class="price-line">Page Development</div><div class="price-line">3 User</div><div class="price-line">Free Update</div>
  </div>
</section>

<section class="slide c2 r2">
  <h2 class="heading">Your Title Goes Here</h2>
  <p class="abs txt" style="left:17px;top:25px;width:190px;font-size:2.4px">Description: Add a short note that explains the figures below and how they should be read.</p>
  <div class="abs" style="left:17px;top:32px;width:194px">
    <table class="data">
      <tr><th>Lorem ipsum</th><th>Value</th><th>Value</th><th>Value</th><th>Value</th></tr>
      <tr><td>Lorem ipsum</td><td>10</td><td>11</td><td>16</td><td>26</td></tr>
      <tr><td>Lorem ipsum</td><td>12</td><td>13</td><td>16</td><td>36</td></tr>
      <tr><td>Lorem ipsum</td><td>20</td><td>22</td><td>12</td><td>21</td></tr>
      <tr><td>Lorem ipsum</td><td>10</td><td>23</td><td>12</td><td>21</td></tr>
      <tr><td>Lorem ipsum</td><td>25</td><td>21</td><td>15</td><td>25</td></tr>
      <tr><td>Lorem ipsum</td><td>12</td><td>20</td><td>16</td><td>21</td></tr>
      <tr><td>Lorem ipsum</td><td>26</td><td>25</td><td>26</td><td>32</td></tr>
      <tr><td>Lorem ipsum</td><td>20</td><td>26</td><td>16</td><td>32</td></tr>
      <tr><td>Lorem ipsum</td><td>12</td><td>15</td><td>12</td><td>32</td></tr>
    </table>
  </div>
  <div class="footer"><div class="brand"><span class="dot"></span>Corvant</div><div class="copy">© Copyright 2024 Corvant. All rights reserved</div><div class="pager"></div></div>
</section>

<section class="slide c3 r2">
  <h2 class="heading">Our Team</h2>
  <div class="photo ph-person round" role="img" aria-label="Team member portrait" style="left:14px;top:26px;width:20px;height:20px"></div>
  <div class="abs" style="left:38px;top:27px;width:68px"><p class="member-name">Evan Hale</p><p class="member-role">CEO</p><p class="txt">Leads strategy and client growth.<br>Key partner relations.<br>Board reporting.</p></div>
  <div class="photo ph-person round" role="img" aria-label="Team member portrait" style="left:116px;top:26px;width:20px;height:20px"></div>
  <div class="abs" style="left:140px;top:27px;width:68px"><p class="member-name">Noah Reid</p><p class="member-role">Manager</p><p class="txt">Runs delivery and planning.<br>Team scheduling.<br>Quality reviews.</p></div>
  <div class="photo ph-person round" role="img" aria-label="Team member portrait" style="left:14px;top:66px;width:20px;height:20px"></div>
  <div class="abs" style="left:38px;top:67px;width:68px"><p class="member-name">Lena Marsh</p><p class="member-role">Head of Recruiting</p><p class="txt">Builds candidate pipelines.<br>Client hiring plans.<br>Talent insights.</p></div>
  <div class="photo ph-person round" role="img" aria-label="Team member portrait" style="left:116px;top:66px;width:20px;height:20px"></div>
  <div class="abs" style="left:140px;top:67px;width:68px"><p class="member-name">Owen Pratt</p><p class="member-role">Tech Lead</p><p class="txt">Guides consulting work.<br>Cloud architecture.<br>Security advice.</p></div>
  <div class="footer"><div class="brand"><span class="dot"></span>Corvant</div><div class="copy">© Copyright 2024 Corvant. All rights reserved</div><div class="pager"></div></div>
</section>

<!-- Row 3 -->
<section class="slide c1 r3">
  <h2 class="heading">Customer Testimonials</h2>
  <div class="photo ph-person round" role="img" aria-label="Client portrait" style="left:51px;top:27px;width:28px;height:28px"></div>
  <p class="abs txt" style="left:100px;top:32px;width:110px">A short quote from a satisfied client goes here, describing the results delivered and the value of working together on the project.</p>
  <div class="blue-band" style="left:0;right:0;top:68px;bottom:0"></div>
  <div class="icon-ring" style="left:50px;top:80px"></div>
  <div class="icon-ring" style="left:93px;top:80px"></div>
  <div class="icon-ring" style="left:136px;top:80px"></div>
  <div class="icon-ring" style="left:179px;top:80px"></div>
  <p class="abs txt-w" style="left:44px;top:97px;width:26px;text-align:center;font-size:2.4px">Why are clients choosing our team?</p>
  <p class="abs txt-w" style="left:87px;top:97px;width:26px;text-align:center;font-size:2.4px">Why do teams hire us for roles?</p>
  <p class="abs txt-w" style="left:130px;top:97px;width:26px;text-align:center;font-size:2.4px">Why do banks trust our advice?</p>
  <p class="abs txt-w" style="left:173px;top:97px;width:26px;text-align:center;font-size:2.4px">Why is the government a partner?</p>
</section>

<section class="slide c2 r3">
  <h2 class="heading">Two Pictures Slide</h2>
  <div class="photo ph-office" role="img" aria-label="Team working at computers" style="left:16px;top:24px;width:95px;height:89px"></div>
  <div class="photo ph-desk" role="img" aria-label="Hands using a tablet" style="left:115px;top:24px;width:96px;height:89px"></div>
  <div class="footer"><div class="brand"><span class="dot"></span>Corvant</div><div class="copy">© Copyright 2024 Corvant. All rights reserved</div><div class="pager"></div></div>
</section>

<section class="slide c3 r3">
  <h2 class="heading">Title And Image + Text</h2>
  <div class="photo ph-desk" role="img" aria-label="Consultant with headset at laptop" style="left:16px;top:24px;width:198px;height:48px"></div>
  <p class="abs lead" style="left:16px;top:78px;width:92px;font-size:3.8px">Place your short statement here, tell the audience what your team does best for clients.</p>
  <p class="abs txt" style="left:118px;top:78px;width:96px">Supporting text goes here to give more detail about the service, the process and the results that clients can expect from each project.</p>
  <div class="footer"><div class="brand"><span class="dot"></span>Corvant</div><div class="copy">© Copyright 2024 Corvant. All rights reserved</div><div class="pager"></div></div>
</section>

<!-- Row 4 -->
<section class="slide c1 r4">
  <h2 class="heading">Sales Comparison</h2>
  <svg class="abs" style="left:0;top:0" width="229" height="131" viewBox="0 0 229 131" aria-label="Sales comparison bar charts">
    <text x="50" y="36" font-size="3.2" fill="#777" text-anchor="middle" font-family="Raleway">2017 Sales</text>
    <rect x="19" y="52" width="6" height="43" fill="#4a7aab"/>
    <rect x="31" y="60" width="6" height="35" fill="#4a7aab"/>
    <rect x="43" y="64" width="6" height="31" fill="#4a7aab"/>
    <rect x="55" y="56" width="6" height="39" fill="#4a7aab"/>
    <rect x="67" y="54" width="6" height="41" fill="#4a7aab"/>
    <line x1="16" y1="95" x2="77" y2="95" stroke="#ccc" stroke-width=".4"/>
    <line x1="114" y1="34" x2="114" y2="100" stroke="#bbb" stroke-width=".4" stroke-dasharray="1 1"/>
    <ellipse cx="114" cy="66" rx="10" ry="6" fill="#6e6e6e"/>
    <text x="114" y="67.5" font-size="3.6" fill="#fff" text-anchor="middle" font-family="Raleway">VS</text>
    <text x="179" y="36" font-size="3.2" fill="#777" text-anchor="middle" font-family="Raleway">2018 Sales</text>
    <rect x="149" y="52" width="6" height="43" fill="#111"/>
    <rect x="161" y="60" width="6" height="35" fill="#111"/>
    <rect x="173" y="64" width="6" height="31" fill="#111"/>
    <rect x="185" y="56" width="6" height="39" fill="#111"/>
    <rect x="197" y="50" width="6" height="45" fill="#111"/>
    <line x1="146" y1="95" x2="207" y2="95" stroke="#ccc" stroke-width=".4"/>
  </svg>
  <p class="abs" style="left:18px;top:101px;font-size:9px;color:var(--blue)">45%</p>
  <p class="abs txt" style="left:46px;top:103px;width:40px">Short note on sales for this year.</p>
  <p class="abs" style="left:148px;top:101px;font-size:9px;color:var(--ink)">68%</p>
  <p class="abs txt" style="left:176px;top:103px;width:40px">Short note on sales for this year.</p>
  <div class="footer"><div class="brand"><span class="dot"></span>Corvant</div><div class="copy">© Copyright 2024 Corvant. All rights reserved</div><div class="pager"></div></div>
</section>

<section class="slide c2 r4">
  <div class="photo" role="img" aria-label="Blurred office background" style="inset:0;background:linear-gradient(160deg,#c9c9c9,#9a9a9a)"></div>
  <p class="abs white-title" style="left:0;right:0;top:22px;text-align:center;font-size:6.4px;font-weight:400">Your Title Goes Here</p>
  <div class="abs" style="left:0;top:64px;width:76px;bottom:0;background:var(--blue);padding:5px 6px"><p class="txt-w">Describe the first key idea here in a few short lines of text so the audience can follow it quickly.</p></div>
  <div class="abs" style="left:76px;top:64px;width:77px;bottom:0;background:#2f2f2f;padding:5px 6px"><p class="txt-w">Describe the second key idea here in a few short lines of text so the audience can follow it quickly.</p></div>
  <div class="abs" style="left:153px;top:64px;right:0;bottom:0;background:#7a7a7a;padding:5px 6px"><p class="txt-w">Describe the third key idea here in a few short lines of text so the audience can follow it quickly.</p></div>
</section>

<section class="slide c3 r4">
  <div class="blue-band" style="left:0;right:0;top:0;height:58px"></div>
  <div class="abs" style="left:0;right:0;top:14px;display:flex;justify-content:center;align-items:center;gap:3px">
    <span class="round" style="width:9px;height:9px;border:1px solid #fff"></span>
    <span style="font-size:13px;font-weight:700;color:#fff">Corvant</span>
  </div>
  <p class="abs txt-w" style="left:0;right:0;top:38px;text-align:center;font-size:5px">This Is Your Timeline Page</p>
  <p class="abs label" style="left:0;right:0;top:63px;text-align:center;font-size:3px">Your Heading Here</p>
  <p class="abs txt" style="left:74px;top:67px;width:80px;text-align:center">A brief line introducing the timeline and the milestones that follow below.</p>
  <div class="tl-line" style="top:88px;bottom:0"></div>
  <div class="tl-node" style="left:110px;top:106px"></div>
</section>

<!-- Row 5 -->
<section class="slide c1 r5">
  <h2 class="heading">Your Title</h2>
  <div class="photo ph-office" role="img" aria-label="Colleagues around a laptop" style="left:115px;top:0;right:0;height:65px"></div>
  <div class="abs" style="left:15px;top:33px"><span class="bullet-icon" style="position:static;display:inline-block;width:4px;height:4px;background:var(--blue)"></span> <span class="label" style="font-size:3px">Bullet Point</span></div>
  <p class="abs txt" style="left:21px;top:38px;width:85px">A short point explaining one benefit of the service in plain words.</p>
  <div class="blue-band" style="left:0;top:65px;width:115px;bottom:0;padding:5px 7px"><p class="txt-w">Add a longer paragraph here to explain the topic of this slide. Keep it short, clear and focused on what matters most to the client.<br><br>Close with one final supporting line.</p></div>
  <div class="abs" style="left:131px;top:77px"><span style="display:inline-block;width:4px;height:4px;background:var(--ink)"></span> <span style="font-size:3px;color:var(--ink)">Bullet Point</span></div>
  <p class="abs txt" style="left:137px;top:82px;width:80px">A short point explaining one benefit of the service in plain words.</p>
</section>

<section class="slide c2 r5">
  <h2 class="heading">Your Title</h2>
  <div class="photo ph-desk" role="img" aria-label="Laptop on a desk" style="left:114px;top:0;right:0;height:65px"></div>
  <p class="abs label" style="left:15px;top:33px;font-size:3px">● Bullet Point</p>
  <p class="abs txt" style="left:21px;top:38px;width:85px">A short point on the first topic in plain words.</p>
  <p class="abs" style="left:15px;top:66px;font-size:3px;color:var(--ink)">▮ Chart</p>
  <p class="abs txt" style="left:21px;top:71px;width:85px">A short point on the second topic in plain words.</p>
  <p class="abs" style="left:15px;top:99px;font-size:3px;color:var(--ink)">◦ Share</p>
  <p class="abs txt" style="left:21px;top:104px;width:85px">A short point on the third topic in plain words.</p>
  <div class="blue-band" style="left:114px;top:65px;right:0;bottom:0;padding:5px 7px"><p class="txt-w">Add a longer paragraph here to explain the topic of this slide. Keep it short, clear and focused on what matters most.<br><br>Close with one final supporting line.</p></div>
</section>

<section class="slide c3 r5">
  <div class="tl-line" style="top:0;bottom:0"></div>
  <div class="tl-node" style="left:110px;top:10px"></div>
  <p class="abs label" style="left:128px;top:13px;font-size:3px">Your Title</p>
  <p class="abs txt" style="left:30px;top:19px;width:72px;text-align:right">A milestone note goes here with one key detail.</p>
  <div class="tl-node" style="left:110px;top:34px"></div>
  <p class="abs label" style="left:128px;top:36px;font-size:3px">Your Title</p>
  <p class="abs big-num" style="left:128px;top:41px">85%</p>
  <p class="abs txt" style="left:128px;top:50px;width:72px">A milestone note goes here with one key detail.</p>
  <div class="tl-node" style="left:110px;top:72px"></div>
  <p class="abs label" style="left:84px;top:74px;font-size:3px">Your Title</p>
  <div class="blue-band" style="left:44px;top:86px;width:60px;height:23px;padding:4px"><p class="txt-w" style="text-align:center">A milestone note goes here with one key detail.</p></div>
</section>

<!-- Row 6 -->
<section class="slide c1 r6">
  <h2 class="heading">Who We Are?</h2>
  <div class="abs" style="left:18px;top:25px;width:50px"><p class="lead" style="font-size:5px">A Title About Contents</p><p class="txt">Subtitle here</p></div>
  <div class="abs" style="left:71px;top:27px;width:142px;border-top:.5px solid var(--blue);padding-top:1px"><p class="txt">2016<br>Explain this part of the story in one or two short lines for the reader.</p></div>
  <div class="abs" style="left:18px;top:55px;width:50px"><p class="lead" style="font-size:5px;color:var(--ink)">A Title About Contents</p><p class="txt">Subtitle here</p></div>
  <div class="abs" style="left:71px;top:57px;width:142px;border-top:.5px solid var(--ink);padding-top:1px"><p class="txt">2017<br>Explain this part of the story in one or two short lines for the reader.</p></div>
  <div class="abs" style="left:18px;top:85px;width:50px"><p class="lead" style="font-size:5px">A Title About Contents</p><p class="txt">Subtitle here</p></div>
  <div class="abs" style="left:71px;top:87px;width:142px;border-top:.5px solid var(--grey);padding-top:1px"><p class="txt">2018<br>Explain this part of the story in one or two short lines for the reader.</p></div>
  <div class="footer"><div class="brand"><span class="dot"></span>Corvant</div><div class="copy">© Copyright 2024 Corvant. All rights reserved</div><div class="pager"></div></div>
</section>

<section class="slide c2 r6">
  <h2 class="heading">Bullet &amp; Chart Area</h2>
  <svg class="abs" style="left:30px;top:28px" width="70" height="70" viewBox="0 0 42 42" aria-label="Pie chart">
    <circle cx="21" cy="21" r="15.9" fill="none" stroke="#4a7aab" stroke-width="31.8" stroke-dasharray="60 40" stroke-dashoffset="25" transform="scale(.5) translate(21 21)"/>
    <circle cx="21" cy="21" r="15.9" fill="none" stroke="#111" stroke-width="31.8" stroke-dasharray="25 75" stroke-dashoffset="-35" transform="scale(.5) translate(21 21)"/>
    <circle cx="21" cy="21" r="15.9" fill="none" stroke="#6b6b6b" stroke-width="31.8" stroke-dasharray="10 90" stroke-dashoffset="-60" transform="scale(.5) translate(21 21)"/>
    <circle cx="21" cy="21" r="15.9" fill="none" stroke="#bdbdbd" stroke-width="31.8" stroke-dasharray="5 95" stroke-dashoffset="-70" transform="scale(.5) translate(21 21)"/>
  </svg>
  <p class="abs" style="left:45px;top:26px;font-size:5px;color:#888">10%</p>
  <p class="abs" style="left:22px;top:45px;font-size:5px;color:#555">15%</p>
  <p class="abs" style="left:23px;top:75px;font-size:5px;color:#222">25%</p>
  <p class="abs" style="left:94px;top:64px;font-size:5px;color:var(--blue)">60%</p>
  <span class="bullet-icon" style="left:125px;top:30px;background:var(--blue)"></span>
  <p class="abs label" style="left:136px;top:30px;font-size:3px">Category One</p><p class="abs txt" style="left:136px;top:34px;width:70px">A short line describing this group.</p>
  <span class="bullet-icon" style="left:125px;top:48px;background:var(--black)"></span>
  <p class="abs label" style="left:136px;top:48px;font-size:3px">Category Two</p><p class="abs txt" style="left:136px;top:52px;width:70px">A short line describing this group.</p>
  <span class="bullet-icon" style="left:125px;top:66px;background:var(--grey)"></span>
  <p class="abs label" style="left:136px;top:66px;font-size:3px">Category Three</p><p class="abs txt" style="left:136px;top:70px;width:70px">A short line describing this group.</p>
  <span class="bullet-icon" style="left:125px;top:84px;background:var(--grey-light)"></span>
  <p class="abs label" style="left:136px;top:84px;font-size:3px">Category Four</p><p class="abs txt" style="left:136px;top:88px;width:70px">A short line describing this group.</p>
  <div class="footer"><div class="brand"><span class="dot"></span>Corvant</div><div class="copy">© Copyright 2024 Corvant. All rights reserved</div><div class="pager"></div></div>
</section>

<section class="slide c3 r6">
  <div class="tl-line" style="top:0;height:60px"></div>
  <div class="tl-node" style="left:110px;top:14px"></div>
  <p class="abs" style="left:124px;top:13px;font-size:5px;color:var(--blue)">Your<br>Title Here</p>
  <p class="abs txt" style="left:124px;top:26px;width:80px">A milestone note goes here with one key detail.</p>
  <div class="tl-node" style="left:110px;top:38px"></div>
  <p class="abs label" style="left:84px;top:41px;font-size:3px;text-align:right">Timeline<br>Finish</p>
  <p class="abs big-num" style="left:86px;top:48px">50%</p>
  <p class="abs txt" style="left:30px;top:44px;width:52px;text-align:right">A milestone note with one key detail.</p>
  <div class="tl-node" style="left:110px;top:58px"></div>
  <p class="abs label" style="left:124px;top:58px;font-size:3px">Your Title</p>
  <p class="abs txt" style="left:124px;top:62px;width:80px">A milestone note with one key detail.</p>
  <div class="abs" style="left:0;right:0;top:86px;display:flex;justify-content:center;align-items:center;gap:4px">
    <span class="round" style="width:14px;height:14px;border:1.4px solid var(--blue)"></span>
    <span style="font-size:20px;font-weight:700;color:var(--blue)">Corvant</span>
  </div>
</section>

<!-- Row 7 -->
<section class="slide c1 r7">
  <h2 class="heading">Bullet &amp; Chart Area</h2>
  <svg class="abs" style="left:0;top:0" width="229" height="131" viewBox="0 0 229 131" aria-label="Horizontal bar chart">
    <g font-size="2.4" fill="#888" font-family="Raleway">
      <text x="10" y="36">Category 1</text><text x="10" y="55">Category 2</text><text x="10" y="74">Category 3</text><text x="10" y="93">Category 4</text>
    </g>
    <line x1="24" y1="28" x2="24" y2="100" stroke="#ccc" stroke-width=".4"/>
    <rect x="24" y="31" width="72" height="2.4" fill="#4a7aab"/><rect x="24" y="34" width="55" height="2.4" fill="#111"/><rect x="24" y="37" width="40" height="2.4" fill="#7b7b7b"/>
    <rect x="24" y="50" width="50" height="2.4" fill="#4a7aab"/><rect x="24" y="53" width="68" height="2.4" fill="#111"/><rect x="24" y="56" width="45" height="2.4" fill="#7b7b7b"/>
    <rect x="24" y="69" width="62" height="2.4" fill="#4a7aab"/><rect x="24" y="72" width="42" height="2.4" fill="#111"/><rect x="24" y="75" width="58" height="2.4" fill="#7b7b7b"/>
    <rect x="24" y="88" width="38" height="2.4" fill="#4a7aab"/><rect x="24" y="91" width="60" height="2.4" fill="#111"/><rect x="24" y="94" width="48" height="2.4" fill="#7b7b7b"/>
    <g font-size="2.2" fill="#888" font-family="Raleway"><circle cx="44" cy="106" r="1" fill="#4a7aab"/><text x="46" y="107">Series 1</text><circle cx="58" cy="106" r="1" fill="#111"/><text x="60" y="107">Series 2</text><circle cx="72" cy="106" r="1" fill="#7b7b7b"/><text x="74" y="107">Series 3</text></g>
  </svg>
  <span class="bullet-icon" style="left:128px;top:30px;background:var(--blue)"></span><p class="abs label" style="left:139px;top:30px;font-size:3px">Category One</p><p class="abs txt" style="left:139px;top:34px;width:70px">A short line describing this group.</p>
  <span class="bullet-icon" style="left:128px;top:48px;background:var(--black)"></span><p class="abs label" style="left:139px;top:48px;font-size:3px">Category Two</p><p class="abs txt" style="left:139px;top:52px;width:70px">A short line describing this group.</p>
  <span class="bullet-icon" style="left:128px;top:66px;background:var(--grey)"></span><p class="abs label" style="left:139px;top:66px;font-size:3px">Category Three</p><p class="abs txt" style="left:139px;top:70px;width:70px">A short line describing this group.</p>
  <span class="bullet-icon" style="left:128px;top:84px;background:var(--grey-light)"></span><p class="abs label" style="left:139px;top:84px;font-size:3px">Category Four</p><p class="abs txt" style="left:139px;top:88px;width:70px">A short line describing this group.</p>
  <div class="footer"><div class="brand"><span class="dot"></span>Corvant</div><div class="copy">© Copyright 2024 Corvant. All rights reserved</div><div class="pager"></div></div>
</section>

<section class="slide c2 r7">
  <h2 class="heading">Bullet &amp; Chart Area</h2>
  <span class="bullet-icon" style="left:15px;top:26px;background:var(--blue)"></span><p class="abs label" style="left:27px;top:26px;font-size:3px">Your Text Here</p><p class="abs txt" style="left:27px;top:30px;width:75px">A short line describing this point.</p>
  <span class="bullet-icon" style="left:15px;top:44px;background:var(--black)"></span><p class="abs label" style="left:27px;top:44px;font-size:3px">Your Text Here</p><p class="abs txt" style="left:27px;top:48px;width:75px">A short line describing this point.</p>
  <span class="bullet-icon" style="left:15px;top:62px;background:var(--grey)"></span><p class="abs label" style="left:27px;top:62px;font-size:3px">Your Text Here</p><p class="abs txt" style="left:27px;top:66px;width:75px">A short line describing this point.</p>
  <span class="bullet-icon" style="left:15px;top:80px;background:var(--grey-light)"></span><p class="abs label" style="left:27px;top:80px;font-size:3px">Your Text Here</p><p class="abs txt" style="left:27px;top:84px;width:75px">A short line describing this point.</p>
  <svg class="abs" style="left:0;top:0" width="229" height="131" viewBox="0 0 229 131" aria-label="Column chart">
    <rect x="125" y="52" width="4" height="40" fill="#4a7aab"/><rect x="129" y="70" width="4" height="22" fill="#111"/><rect x="133" y="62" width="4" height="30" fill="#7b7b7b"/>
    <rect x="146" y="60" width="4" height="32" fill="#4a7aab"/><rect x="150" y="66" width="4" height="26" fill="#111"/><rect x="154" y="54" width="4" height="38" fill="#7b7b7b"/>
    <rect x="167" y="58" width="4" height="34" fill="#4a7aab"/><rect x="171" y="68" width="4" height="24" fill="#111"/><rect x="175" y="56" width="4" height="36" fill="#7b7b7b"/>
    <rect x="188" y="54" width="4" height="38" fill="#4a7aab"/><rect x="192" y="64" width="4" height="28" fill="#111"/><rect x="196" y="44" width="4" height="48" fill="#7b7b7b"/>
    <line x1="122" y1="92" x2="204" y2="92" stroke="#ccc" stroke-width=".4"/>
    <g font-size="2.2" fill="#888" font-family="Raleway"><text x="126" y="96">Category 1</text><text x="147" y="96">Category 2</text><text x="168" y="96">Category 3</text><text x="189" y="96">Category 4</text>
    <circle cx="150" cy="101" r="1" fill="#4a7aab"/><text x="152" y="102">Series 1</text><circle cx="163" cy="101" r="1" fill="#111"/><text x="165" y="102">Series 2</text><circle cx="176" cy="101" r="1" fill="#7b7b7b"/><text x="178" y="102">Series 3</text></g>
  </svg>
  <div class="footer"><div class="brand"><span class="dot"></span>Corvant</div><div class="copy">© Copyright 2024 Corvant. All rights reserved</div><div class="pager"></div></div>
</section>

<section class="slide c3 r7">
  <h2 class="heading">Column Chart</h2>
  <svg class="abs" style="left:0;top:0" width="229" height="131" viewBox="0 0 229 131" aria-label="Column chart by category">
    <g font-size="3" fill="#555" font-family="Raleway" text-anchor="middle">
      <rect x="12" y="27" width="8" height="62" fill="#4a7aab"/><text x="16" y="25">43</text>
      <rect x="22" y="60" width="8" height="29" fill="#111"/><text x="26" y="58">20</text>
      <rect x="32" y="60" width="8" height="29" fill="#7b7b7b"/><text x="36" y="58">20</text>
      <rect x="65" y="55" width="8" height="34" fill="#4a7aab"/><text x="69" y="53">23</text>
      <rect x="75" y="25" width="8" height="64" fill="#111"/><text x="79" y="23">44</text>
      <rect x="85" y="57" width="8" height="32" fill="#7b7b7b"/><text x="89" y="55">22</text>
      <rect x="117" y="38" width="8" height="51" fill="#4a7aab"/><text x="121" y="36">36</text>
      <rect x="127" y="62" width="8" height="27" fill="#111"/><text x="131" y="60">19</text>
      <rect x="137" y="24" width="8" height="65" fill="#7b7b7b"/><text x="141" y="22">45</text>
      <rect x="169" y="10" width="8" height="79" fill="#4a7aab"/><text x="173" y="9">54</text>
      <rect x="179" y="49" width="8" height="40" fill="#111"/><text x="183" y="47">28</text>
      <rect x="189" y="42" width="8" height="47" fill="#7b7b7b"/><text x="193" y="40">33</text>
    </g>
    <line x1="8" y1="89" x2="220" y2="89" stroke="#ccc" stroke-width=".4"/>
    <g font-size="2.4" fill="#4a7aab" font-family="Raleway" text-anchor="middle"><text x="26" y="93">Category 1</text><text x="79" y="93">Category 2</text><text x="131" y="93">Category 3</text><text x="183" y="93">Category 4</text></g>
  </svg>
  <p class="abs txt" style="left:8px;top:95px;width:40px;text-align:center">A short note for this category.</p>
  <p class="abs txt" style="left:60px;top:95px;width:40px;text-align:center">A short note for this category.</p>
  <p class="abs txt" style="left:112px;top:95px;width:40px;text-align:center">A short note for this category.</p>
  <p class="abs txt" style="left:164px;top:95px;width:40px;text-align:center">A short note for this category.</p>
  <div class="footer"><div class="brand"><span class="dot"></span>Corvant</div><div class="copy">© Copyright 2024 Corvant. All rights reserved</div><div class="pager"></div></div>
</section>

<!-- Row 8 -->
<section class="slide c1 r8">
  <h2 class="heading">Three Steps</h2>
  <span class="bullet-icon" style="left:13px;top:28px;background:var(--blue)"></span><p class="abs label" style="left:25px;top:28px;font-size:3px">Sample Text</p><p class="abs txt" style="left:25px;top:32px;width:105px">Describe the first step of the process in two short lines for the reader.</p>
  <span class="bullet-icon" style="left:13px;top:51px;background:var(--black)"></span><p class="abs label" style="left:25px;top:51px;font-size:3px">Sample Text</p><p class="abs txt" style="left:25px;top:55px;width:105px">Describe the second step of the process in two short lines for the reader.</p>
  <span class="bullet-icon" style="left:13px;top:74px;background:var(--grey)"></span><p class="abs label" style="left:25px;top:74px;font-size:3px">Sample Text</p><p class="abs txt" style="left:25px;top:78px;width:105px">Describe the third step of the process in two short lines for the reader.</p>
  <svg class="abs" style="left:140px;top:12px" width="85" height="102" viewBox="0 0 85 102" aria-label="Three step rings">
    <circle cx="56" cy="24" r="17" fill="none" stroke="#4a7aab" stroke-width="10"/>
    <circle cx="28" cy="50" r="17" fill="none" stroke="#111" stroke-width="10"/>
    <circle cx="56" cy="76" r="17" fill="none" stroke="#6b6b6b" stroke-width="10"/>
  </svg>
  <div class="footer"><div class="brand"><span class="dot"></span>Corvant</div><div class="copy">© Copyright 2024 Corvant. All rights reserved</div><div class="pager"></div></div>
</section>

<section class="slide c2 r8">
  <h2 class="heading">Project Timeline</h2>
  <svg class="abs" style="left:0;top:0" width="229" height="131" viewBox="0 0 229 131" aria-label="Gantt chart project timeline">
    <g font-size="2.4" fill="#777" font-family="Raleway">
      <text x="22" y="32">Project start</text>
      <text x="67" y="32">Jan</text><text x="80" y="32">Feb</text><text x="93" y="32">Mar</text><text x="106" y="32">Apr</text><text x="119" y="32">May</text><text x="132" y="32">June</text><text x="145" y="32">July</text><text x="158" y="32">Aug</text><text x="171" y="32">Sep</text><text x="184" y="32">Oct</text><text x="197" y="32">Nov</text>
      <text x="22" y="39">Process 1</text><text x="22" y="46">Process 2</text><text x="22" y="53">Process 3</text><text x="22" y="60">Process 4</text><text x="22" y="67">Process 5</text><text x="22" y="74">Process 6</text><text x="22" y="81">Process 7</text><text x="22" y="88">Process 8</text><text x="22" y="95">Process 9</text>
    </g>
    <g stroke="#e6e6e6" stroke-width=".3">
      <line x1="20" y1="34" x2="210" y2="34"/><line x1="20" y1="41" x2="210" y2="41"/><line x1="20" y1="48" x2="210" y2="48"/><line x1="20" y1="55" x2="210" y2="55"/><line x1="20" y1="62" x2="210" y2="62"/><line x1="20" y1="69" x2="210" y2="69"/><line x1="20" y1="76" x2="210" y2="76"/><line x1="20" y1="83" x2="210" y2="83"/><line x1="20" y1="90" x2="210" y2="90"/><line x1="20" y1="97" x2="210" y2="97"/>
    </g>
    <rect x="70" y="36.5" width="22" height="2" fill="#4a7aab"/>
    <rect x="168" y="36.5" width="20" height="2" fill="#111"/>
    <rect x="84" y="43.5" width="46" height="2" fill="#7b7b7b"/>
    <rect x="96" y="50.5" width="72" height="2" fill="#111"/>
    <rect x="110" y="57.5" width="40" height="2" fill="#4a7aab"/>
    <rect x="98" y="64.5" width="46" height="2" fill="#111"/>
    <rect x="114" y="71.5" width="22" height="2" fill="#bdbdbd"/>
    <rect x="160" y="78.5" width="40" height="2" fill="#4a7aab"/>
    <rect x="130" y="85.5" width="28" height="2" fill="#7b7b7b"/>
    <rect x="150" y="92.5" width="24" height="2" fill="#4a7aab"/>
    <g font-size="2.2" fill="#888" font-family="Raleway">
      <circle cx="46" cy="104" r="1" fill="#4a7aab"/><text x="48" y="105">Description</text>
      <circle cx="76" cy="104" r="1" fill="#111"/><text x="78" y="105">Description</text>
      <circle cx="106" cy="104" r="1" fill="#7b7b7b"/><text x="108" y="105">Description</text>
      <circle cx="136" cy="104" r="1" fill="#bdbdbd"/><text x="138" y="105">Description</text>
      <circle cx="166" cy="104" r="1" fill="#4a7aab"/><text x="168" y="105">Description</text>
    </g>
  </svg>
  <div class="footer"><div class="brand"><span class="dot"></span>Corvant</div><div class="copy">© Copyright 2024 Corvant. All rights reserved</div><div class="pager"></div></div>
</section>

<section class="slide c3 r8">
  <div class="photo ph-desk" role="img" aria-label="Hands typing on a laptop" style="inset:0"></div>
  <div class="abs" style="left:114px;top:0;right:0;bottom:0;background:rgba(74,122,171,.92);padding:20px 10px 0 14px">
    <p class="white-title" style="font-size:6px;margin-bottom:6px">Key Points</p>
    <p class="txt-w" style="line-height:2.6">• Deliver clear results<br>• Hire trusted experts<br>• Advise on cloud plans<br>• Secure client systems<br>• Support every project<br>• Grow lasting teams<br>• Report with clarity</p>
  </div>
</section>

<!-- Row 9 -->
<section class="slide c1 r9">
  <h2 class="heading">Three Bullets Area</h2>
  <div class="photo ph-office" role="img" aria-label="Team meeting around a table" style="left:0;right:0;top:25px;height:53px"></div>
  <span class="abs round" style="left:31px;top:71px;width:14px;height:14px;background:var(--blue)"></span>
  <span class="abs round" style="left:108px;top:71px;width:14px;height:14px;background:var(--black)"></span>
  <span class="abs round" style="left:184px;top:71px;width:14px;height:14px;background:#fff;box-shadow:0 0 0 .5px #ccc"></span>
  <p class="abs txt" style="left:13px;top:89px;width:50px;text-align:center">A short note that sums up this point for the reader.</p>
  <p class="abs txt" style="left:90px;top:89px;width:50px;text-align:center">A short note that sums up this point for the reader.</p>
  <p class="abs txt" style="left:166px;top:89px;width:50px;text-align:center">A short note that sums up this point for the reader.</p>
  <div class="footer"><div class="brand"><span class="dot"></span>Corvant</div><div class="copy">© Copyright 2024 Corvant. All rights reserved</div><div class="pager"></div></div>
</section>

<section class="slide c2 r9">
  <h2 class="heading">Your Blank slide</h2>
  <span class="abs round" style="left:118px;top:52px;width:66px;height:66px;border:6px solid #f1f3f6"></span>
  <div class="footer"><div class="brand"><span class="dot"></span>Corvant</div><div class="copy">© Copyright 2024 Corvant. All rights reserved</div><div class="pager"></div></div>
</section>

<section class="slide c3 r9" style="background:var(--blue)">
  <div class="photo" role="img" aria-label="Faded workspace background" style="inset:0;background:linear-gradient(135deg,#5b88b4,#3d6893)"></div>
  <p class="abs white-title" style="left:14px;top:30px;font-size:12px;font-weight:600">Thank You</p>
  <p class="abs txt-w" style="left:14px;top:46px;font-size:4.2px">Send Your Feedback</p>
  <p class="abs txt-w" style="left:14px;top:76px;font-size:2.6px;line-height:2.2">⌖ 12 Harbour Road, Suite 4<br>✆ 555 0142 000<br>✉ hello@corvant.example<br>◎ www.corvant.example</p>
  <div class="abs" style="left:140px;top:40px;display:flex;flex-direction:column;align-items:center;gap:4px">
    <span class="round" style="width:22px;height:22px;border:2px solid #fff"></span>
    <span style="font-size:15px;font-weight:700;color:#fff">Corvant</span>
  </div>
</section>

</body>
</html>
```